Real Estate Agent Service Brochure

I need a trifold brochure to showcase my real estate services. I am a veteran Real Estate Broker specializing in marketing properties for sale and for top dollar. I would like to see designs that use colors from my logo (attached) and I would like to showcase some before and after photos of staging jobs I have done to homes to get them ready for the market. This brochure is specific to home sellers. You are happy to go check out my website for inspiration www.lomavertpa.com but keep the copy as I have written it. The the final design should communicate experienced professional who uses current technologies and strategies to market properties for the highest value.

Target Market(s)

Homeowners wanting to sell their homes

Industry/Entity Type

Real Estate Agent

Font styles to use
Serif

Requirements
Must have
• My, logo, personal photo, title and contact information as listed:
• Marta Venholt
• Owner Broker
• Stager Re-Designer
• 860-912-7048
• BRAVE Realty LLC
• LOMAVERTPA.com
• Marta@LOMAVERTPA.com
• The colors used should be those in my logo.
• Brochure should be able to fit in standard envelope for mailing.
Nice to have
• I think I would like my personal photo and contact information on the front panel.
Should not have
• Bright colors.

```html
<!DOCTYPE html>
<html lang="en">
<head>
<meta charset="utf-8">
<title>Marta Venholt – Seller Brochure Inside Spread</title>
<link href="https://fonts.googleapis.com/css2?family=Exo+2:ital,wght@0,300;0,400;0,700;1,200;1,300&display=swap" rel="stylesheet">
<style>
  :root {
    --paper: #ffffff;
    --ink: #1d1b22;
    --plum: #6b6078;
    --navy: #141a3f;
    --ring-grey: #b9b2ae;
    --line-grey: #a7a5ab;
    --label-grey: #7a777c;
    --white: #ffffff;
  }
  html, body {
    margin: 0;
    padding: 0;
    overflow: hidden;
    background: var(--paper);
  }
  .spread {
    position: relative;
    width: 1200px;
    height: 1000px;
    overflow: hidden;
    background: var(--paper);
    font-family: "Exo 2", sans-serif;
    color: var(--ink);
  }
  .artwork {
    position: absolute;
    inset: 0;
  }
  .copy {
    position: absolute;
    margin: 0;
    font-size: 16px;
    font-weight: 300;
    line-height: 21.3px;
  }
  .copy strong { font-weight: 700; }
  .intro { left: 42px; top: 79px; width: 330px; }
  .approach { left: 826px; top: 79px; width: 330px; }
  .approach p { margin: 0 0 12px; }
  .value { left: 434px; top: 540px; width: 320px; }
  .stage-label {
    position: absolute;
    font-size: 12px;
    letter-spacing: 1px;
    color: var(--label-grey);
    font-weight: 400;
  }
  .contact {
    position: absolute;
    left: 40px;
    top: 772px;
    width: 346px;
    text-align: center;
    color: var(--white);
  }
  .contact-name {
    margin: 0 0 2px;
    font-size: 28px;
    font-weight: 200;
    font-style: italic;
    line-height: 36px;
  }
  .contact-title {
    margin: 0;
    font-size: 17px;
    font-weight: 700;
    line-height: 20px;
  }
  .contact-lines {
    margin: 0;
    font-size: 14.5px;
    font-weight: 300;
    line-height: 18px;
  }
</style>
</head>
<body>
<main class="spread">
  <svg class="artwork" width="1200" height="1000" viewBox="0 0 1200 1000" aria-hidden="false">
    <defs>
      <radialGradient id="bedroom-before-tone" cx="50%" cy="40%" r="60%">
        <stop offset="0" stop-color="#d8d2c6"/>
        <stop offset="0.6" stop-color="#8f8779"/>
        <stop offset="1" stop-color="#2a211b"/>
      </radialGradient>
      <linearGradient id="bedroom-after-tone" x1="0" y1="0" x2="0" y2="1">
        <stop offset="0" stop-color="#d9d4cc"/>
        <stop offset="0.5" stop-color="#c9c2b5"/>
        <stop offset="1" stop-color="#eeeeee"/>
      </linearGradient>
      <linearGradient id="basement-after-tone" x1="0" y1="0" x2="0" y2="1">
        <stop offset="0" stop-color="#c99534"/>
        <stop offset="0.5" stop-color="#e7b660"/>
        <stop offset="1" stop-color="#c79d68"/>
      </linearGradient>
      <radialGradient id="basement-before-tone" cx="50%" cy="45%" r="60%">
        <stop offset="0" stop-color="#b08652"/>
        <stop offset="1" stop-color="#4a2f1e"/>
      </radialGradient>
      <linearGradient id="portrait-tone" x1="0" y1="0" x2="0" y2="1">
        <stop offset="0" stop-color="#6e5a4a"/>
        <stop offset="0.55" stop-color="#8c7766"/>
        <stop offset="1" stop-color="#2a2a2e"/>
      </linearGradient>
    </defs>

    <!-- decorative line circles -->
    <g class="guide-lines" fill="none" stroke="var(--line-grey)" stroke-width="1">
      <circle cx="575" cy="240" r="240"/>
      <circle cx="660" cy="430" r="260"/>
      <circle cx="980" cy="230" r="190"/>
      <circle cx="1060" cy="430" r="140"/>
      <circle cx="1020" cy="840" r="160"/>
      <circle cx="300" cy="620" r="330"/>
      <circle cx="1150" cy="330" r="360"/>
      <path d="M360 990 C 500 900, 620 860, 700 820"/>
    </g>

    <!-- plum contact panel -->
    <path class="contact-panel" d="M16 452 C 190 415, 400 690, 412 950 L16 950 Z" fill="var(--plum)"/>

    <!-- bedroom before -->
    <circle cx="198" cy="370" r="125" fill="none" stroke="var(--ring-grey)" stroke-width="2"/>
    <circle cx="198" cy="370" r="112" fill="none" stroke="var(--ring-grey)" stroke-width="12"/>
    <circle cx="198" cy="370" r="105" fill="url(#bedroom-before-tone)" role="img" aria-label="Photo: empty bedroom with dark wood floor before staging"/>

    <!-- bedroom after -->
    <circle cx="575" cy="285" r="208" fill="none" stroke="var(--navy)" stroke-width="1.5"/>
    <circle cx="575" cy="285" r="184" fill="none" stroke="var(--navy)" stroke-width="14"/>
    <circle cx="575" cy="285" r="177" fill="url(#bedroom-after-tone)" role="img" aria-label="Photo: staged bedroom with white bedding and chandelier after staging"/>

    <!-- portrait -->
    <circle cx="205" cy="628" r="105" fill="none" stroke="var(--navy)" stroke-width="1.5"/>
    <circle cx="205" cy="628" r="91" fill="none" stroke="var(--navy)" stroke-width="9"/>
    <circle cx="205" cy="628" r="86" fill="url(#portrait-tone)" role="img" aria-label="Portrait photo of Marta Venholt"/>

    <!-- basement after -->
    <circle cx="785" cy="650" r="166" fill="none" stroke="var(--navy)" stroke-width="1.5"/>
    <circle cx="785" cy="650" r="148" fill="none" stroke="var(--navy)" stroke-width="12"/>
    <circle cx="785" cy="650" r="142" fill="url(#basement-after-tone)" role="img" aria-label="Photo: staged basement family room with treadmill after staging"/>

    <!-- basement before -->
    <circle cx="1043" cy="763" r="112" fill="none" stroke="var(--ring-grey)" stroke-width="1.5"/>
    <circle cx="1043" cy="763" r="98" fill="none" stroke="var(--ring-grey)" stroke-width="12"/>
    <circle cx="1043" cy="763" r="92" fill="url(#basement-before-tone)" role="img" aria-label="Photo: cluttered basement family room before staging"/>
  </svg>

  <span class="stage-label" style="left:173px; top:223px;">BEFORE</span>
  <span class="stage-label" style="left:624px; top:73px; transform:rotate(14deg);">AFTER</span>
  <span class="stage-label" style="left:842px; top:464px; transform:rotate(16deg);">AFTER</span>
  <span class="stage-label" style="left:1028px; top:642px; transform:rotate(4deg);">BEFORE</span>

  <p class="copy intro"><strong>Marta Venholt Residential Marketing Real Estate Specialist</strong> truly understands not only the legal process needed but also recognizes buyer trends and knows how to “showcase” a property to sell targeted to the proper consumer demographic.</p>

  <div class="copy approach">
    <p>Therefore, taking a cookie cutter approach is not acceptable, she recognizes that each property is unique and requires a personalized marketing strategy.</p>
    <p>A veteran in the real estate industry with nearly 30 years of real estate expertise and consistent membership in the Multi-Million-Dollar Club combined with her HSP Home Stager and Re-Designer credentials assures that her clients get the advantage of vast knowledge, seasoned experience and proven results, all geared to creating beautiful spaces, which form a connection with the right buyer producing the highest and best offer.</p>
  </div>

  <p class="copy value">A home is one of<br>your most valuable<br>assets. If you are<br>thinking about<br>selling a property,<br>it is crucial that you<br>hire someone with<br>an extraordinary<br>history of happy<br>sellers. Marta devotes<br>her efforts to selling<br>real estate, by keeping<br>up with the evolving<br>market, researching buyer<br>trends and preparing homes<br>before they enter the market by<br>staging them to connect with the target<br>buyer. Marta knows all sales are not alike.</p>

  <div class="contact">
    <p class="contact-name">Marta Venholt</p>
    <p class="contact-title">Owner Broker</p>
    <p class="contact-lines">Stage Re-Designer<br>860-912-7048<br>BRAVE Realty LLC<br>LOMAVERTPA.com<br>Marta@LOMAVERTPA.com</p>
  </div>
</main>
</body>
</html>
```